Equity, Effectiveness and Efficiency in charitable food relief sector

I am undertaking my PhD in food policy in the charitable food relief sector, specifically investigating the factors (supply, demand and capacity) that affect the introduction of nutrition policy and in turn, affect the sector's ability to achieve equity, effectiveness and efficiency.

I need a graphic device that incorporates this central idea of Equity, Effectiveness and Efficiency, and how the factors of supply, demand and capacity interact. There are sub-factors within supply (1-6), demand (7-10) and capacity (11 - 15). All these details are shown in the attached figure (Basic figure_Eq Effec Effic and factors.jpg)

This figure (Basic figure_Eq Effec Effic and factors.jpg) contains all the information I need in a graphic but I need something that is more visually appealing, and that can link the ideas in a format other than a table. The final graphic will outline how the food relief sector balances the core objectives of equity, effectiveness and efficiency with the factors (and sub-factors) of supply, demand and capacity.

```html
<!DOCTYPE html>
<html lang="en">
<head>
<meta charset="utf-8">
<title>Factors Affecting The Introduction Of Nutrition Policy</title>
<link href="https://fonts.googleapis.com/css2?family=Montserrat:wght@400;500;600;700;800&display=swap" rel="stylesheet">
<style>
  :root{
    --bg:#ffffff;
    --ink:#1a1a1a;
    --ring:#cfcfcf;
    --map:#ececec;
    --supply:#1b78bf;
    --supply-light:#2f9ad8;
    --capacity:#4c9b2f;
    --capacity-light:#7cbf3a;
    --demand:#e8273f;
    --demand-light:#f0506a;
    --demand-ring:#6db446;
    --demand-node:#4f9a31;
    --orange:#f29a1f;
    --orange-node:#d9841a;
    --orange-deep:#ef6d24;
    --white:#ffffff;
  }
  html,body{margin:0;padding:0;overflow:hidden;background:var(--bg);}
  .canvas{width:946px;height:1200px;overflow:hidden;position:relative;}
  .canvas svg{display:block;width:946px;height:1200px;}
  text{font-family:'Montserrat',sans-serif;}
  .title{font-weight:800;font-size:15px;fill:var(--ink);}
  .factor-label{font-size:7.4px;fill:var(--ink);font-weight:500;}
  .node-num{font-size:8px;font-weight:700;fill:var(--white);}
  .venn-label{font-size:9.5px;font-weight:700;fill:var(--white);}
  .core-label{font-size:10px;font-weight:700;fill:#333;}
  .hub-label{font-size:13px;font-weight:700;fill:var(--ink);}
  .seg-label{font-size:7px;font-weight:500;fill:var(--white);}
  .band-label{font-size:7.4px;font-weight:500;fill:var(--white);}
  .arc-caption{font-size:9.6px;font-weight:700;fill:#333;}
  .list-item{font-size:7px;fill:var(--ink);font-weight:500;}
</style>
</head>
<body>
<div class="canvas">
<svg viewBox="0 0 850 1078" xmlns="http://www.w3.org/2000/svg">
  <defs>
    <linearGradient id="supply-fill" x1="0" y1="0" x2="1" y2="1">
      <stop offset="0" stop-color="var(--supply-light)"/>
      <stop offset="1" stop-color="var(--supply)"/>
    </linearGradient>
    <linearGradient id="capacity-fill" x1="1" y1="0" x2="0" y2="1">
      <stop offset="0" stop-color="var(--capacity)"/>
      <stop offset="1" stop-color="var(--capacity-light)"/>
    </linearGradient>
    <linearGradient id="demand-fill" x1="0" y1="0" x2="1" y2="1">
      <stop offset="0" stop-color="var(--demand-light)"/>
      <stop offset="1" stop-color="var(--demand)"/>
    </linearGradient>
    <linearGradient id="band-fill" x1="0" y1="0" x2="1" y2="0">
      <stop offset="0" stop-color="var(--supply)"/>
      <stop offset="0.3" stop-color="var(--supply)"/>
      <stop offset="0.48" stop-color="#3a9a6a"/>
      <stop offset="0.68" stop-color="#c9a52a"/>
      <stop offset="1" stop-color="var(--orange-deep)"/>
    </linearGradient>
    <path id="supply-arc" d="M119 773 A125 125 0 0 0 218 928"/>
    <path id="capacity-arc" d="M461 773 A123 123 0 0 0 559 926"/>
    <path id="demand-arc" d="M305 645 A110 110 0 0 1 443 539"/>
  </defs>

  <!-- ===== Top: circular factor map ===== -->
  <text class="title" x="425" y="62" text-anchor="middle">Factors Affecting The Introducton Of Nutrition Policy</text>

  <rect class="world-map" x="120" y="95" width="620" height="385" rx="40" fill="var(--map)" opacity="0.55" role="img" aria-label="Faint world map in the background"/>

  <circle class="factor-ring" cx="415" cy="280" r="150" fill="none" stroke="var(--ring)" stroke-width="4"/>

  <g class="venn">
    <circle cx="378" cy="258" r="76" fill="url(#supply-fill)" opacity="0.95"/>
    <circle cx="453" cy="258" r="76" fill="url(#capacity-fill)" opacity="0.9"/>
    <circle cx="415" cy="322" r="76" fill="url(#demand-fill)" opacity="0.88"/>
    <circle cx="415" cy="280" r="46" fill="var(--white)"/>
    <text class="venn-label" transform="translate(330 243) rotate(-62)" text-anchor="middle">Supply</text>
    <text class="venn-label" transform="translate(500 243) rotate(62)" text-anchor="middle">Capacity</text>
    <text class="venn-label" x="415" y="370" text-anchor="middle">Demand</text>
    <text class="core-label" x="415" y="272" text-anchor="middle">Equity,</text>
    <text class="core-label" x="415" y="284" text-anchor="middle">Effectiveness,</text>
    <text class="core-label" x="415" y="296" text-anchor="middle">Efficiency</text>
  </g>

  <g class="factor-nodes">
    <g fill="var(--supply)" stroke="var(--white)" stroke-width="2">
      <circle cx="410" cy="130" r="9"/><circle cx="350" cy="143" r="9"/><circle cx="299" cy="181" r="9"/>
      <circle cx="268" cy="235" r="9"/><circle cx="261" cy="297" r="9"/><circle cx="283" cy="356" r="9"/>
    </g>
    <g fill="var(--demand)" stroke="var(--white)" stroke-width="2">
      <circle cx="324" cy="404" r="9"/><circle cx="381" cy="429" r="9"/><circle cx="443" cy="430" r="9"/><circle cx="501" cy="404" r="9"/>
    </g>
    <g fill="var(--capacity)" stroke="var(--white)" stroke-width="2">
      <circle cx="542" cy="356" r="9"/><circle cx="563" cy="296" r="9"/><circle cx="556" cy="234" r="9"/>
      <circle cx="523" cy="180" r="9"/><circle cx="473" cy="142" r="9"/>
    </g>
    <g class="node-num" text-anchor="middle">
      <text x="410" y="133">1</text><text x="350" y="146">2</text><text x="299" y="184">3</text>
      <text x="268" y="238">4</text><text x="261" y="300">5</text><text x="283" y="359">6</text>
      <text x="324" y="407">7</text><text x="381" y="432">8</text><text x="443" y="433">9</text>
      <text x="501" y="407">10</text><text x="542" y="359">11</text><text x="563" y="299">12</text>
      <text x="556" y="237">13</text><text x="523" y="183">14</text><text x="473" y="145">15</text>
    </g>
  </g>

  <g class="factor-labels">
    <text class="factor-label" x="410" y="104" text-anchor="middle">Uncertain</text>
    <text class="factor-label" x="410" y="114" text-anchor="middle">material supply</text>
    <text class="factor-label" x="322" y="123" text-anchor="middle">Uncertain</text>
    <text class="factor-label" x="322" y="133" text-anchor="middle">monetary supply</text>
    <text class="factor-label" x="265" y="172" text-anchor="middle">Limited</text>
    <text class="factor-label" x="265" y="182" text-anchor="middle">food supply</text>
    <text class="factor-label" x="251" y="238" text-anchor="end">Perishability</text>
    <text class="factor-label" x="228" y="293" text-anchor="middle">Donor</text>
    <text class="factor-label" x="228" y="303" text-anchor="middle">constraints</text>
    <text class="factor-label" x="240" y="355" text-anchor="middle">Donor</text>
    <text class="factor-label" x="240" y="365" text-anchor="middle">relationships</text>
    <text class="factor-label" x="293" y="423" text-anchor="middle">Uncertain</text>
    <text class="factor-label" x="293" y="433" text-anchor="middle">demand</text>
    <text class="factor-label" x="370" y="453" text-anchor="middle">Limited</text>
    <text class="factor-label" x="370" y="463" text-anchor="middle">demand visibility</text>
    <text class="factor-label" x="447" y="453" text-anchor="middle">Client</text>
    <text class="factor-label" x="447" y="463" text-anchor="middle">choice</text>
    <text class="factor-label" x="527" y="422" text-anchor="middle">Food</text>
    <text class="factor-label" x="527" y="432" text-anchor="middle">wastage</text>
    <text class="factor-label" x="566" y="360">Storage</text>
    <text class="factor-label" x="583" y="299">Transportation</text>
    <text class="factor-label" x="576" y="237">Workforce</text>
    <text class="factor-label" x="548" y="173">External</text>
    <text class="factor-label" x="548" y="183">stakeholders</text>
    <text class="factor-label" x="495" y="127">Budget</text>
  </g>

  <g class="sub-list" stroke="#555" stroke-width="0.7" fill="none">
    <path d="M614 234 H631 M631 212 V259 M631 212 H640 M631 224 H640 M631 236 H640 M631 248 H640 M631 259 H640"/>
    <path d="M598 357 H631 M631 353 V365 M631 353 H640 M631 365 H640"/>
  </g>
  <g fill="var(--capacity)">
    <circle cx="643" cy="212" r="2.2"/><circle cx="643" cy="224" r="2.2"/><circle cx="643" cy="236" r="2.2"/>
    <circle cx="643" cy="248" r="2.2"/><circle cx="643" cy="259" r="2.2"/>
    <circle cx="643" cy="353" r="2.2"/><circle cx="643" cy="365" r="2.2"/>
  </g>
  <g class="list-item">
    <text x="649" y="214">Volunteers</text><text x="649" y="226">Expertise and training</text>
    <text x="649" y="238">Attitudes and Beliefs</text><text x="649" y="250">Collaboration</text>
    <text x="649" y="261">Executive Support</text>
    <text x="649" y="355">Cold</text><text x="649" y="367">Warehouse</text>
  </g>

  <!-- ===== Bottom: flow of three factor cycles ===== -->
  <g class="demand-cycle">
    <circle cx="415" cy="645" r="71" fill="none" stroke="var(--demand-ring)" stroke-width="52" stroke-dasharray="106 5.5" transform="rotate(-42.8 415 645)"/>
    <circle cx="415" cy="645" r="45" fill="var(--white)"/>
    <text class="hub-label" x="415" y="650" text-anchor="middle">Demand</text>
    <text class="arc-caption"><textPath href="#demand-arc">Equity, Effectiveness, Efficiency</textPath></text>
  </g>

  <g class="flow-band">
    <polygon points="62,690 745,690 765,717 745,745 62,745 75,717" fill="url(#band-fill)"/>
  </g>

  <g class="supply-cycle">
    <circle cx="240" cy="805" r="81" fill="none" stroke="var(--supply)" stroke-width="58" stroke-dasharray="80 4.8" transform="rotate(-28.3 240 805)"/>
    <circle cx="240" cy="805" r="52" fill="var(--white)"/>
    <text class="hub-label" x="240" y="810" text-anchor="middle">Supply</text>
    <text class="arc-caption"><textPath href="#supply-arc">Equity, Effectiveness, Efficiency</textPath></text>
  </g>

  <g class="capacity-cycle">
    <circle cx="580" cy="805" r="80" fill="none" stroke="var(--orange)" stroke-width="60" stroke-dasharray="120 5.7" transform="rotate(-32.9 580 805)"/>
    <circle cx="580" cy="805" r="50" fill="var(--white)"/>
    <text class="hub-label" x="580" y="810" text-anchor="middle">Capacity</text>
    <text class="arc-caption"><textPath href="#capacity-arc">Equity, Effectiveness, Efficiency</textPath></text>
  </g>

  <g class="flow-band-labels">
    <text class="band-label" x="157" y="717" text-anchor="middle">Uncertain</text>
    <text class="band-label" x="157" y="727" text-anchor="middle">material supply</text>
    <text class="band-label" x="710" y="722" text-anchor="middle">Budget</text>
  </g>

  <g class="cycle-nodes" stroke="var(--white)" stroke-width="1.5">
    <circle cx="152" cy="690" r="9" fill="var(--supply)"/>
    <circle cx="705" cy="690" r="9" fill="var(--orange-deep)"/>
    <circle cx="267" cy="758" r="9" fill="var(--supply)"/>
    <circle cx="294" cy="805" r="9" fill="var(--supply)"/>
    <circle cx="267" cy="852" r="9" fill="var(--supply)"/>
    <circle cx="213" cy="852" r="9" fill="var(--supply)"/>
    <circle cx="186" cy="805" r="9" fill="var(--supply)"/>
    <circle cx="415" cy="597" r="9" fill="var(--demand-node)"/>
    <circle cx="463" cy="645" r="9" fill="var(--demand-node)"/>
    <circle cx="415" cy="693" r="9" fill="var(--demand-node)"/>
    <circle cx="367" cy="645" r="9" fill="var(--demand-node)"/>
    <circle cx="589" cy="754" r="9" fill="var(--orange-node)"/>
    <circle cx="631" cy="814" r="9" fill="var(--orange-node)"/>
    <circle cx="571" cy="856" r="9" fill="var(--orange-node)"/>
    <circle cx="529" cy="796" r="9" fill="var(--orange-node)"/>
  </g>
  <g class="node-num" text-anchor="middle">
    <text x="152" y="693">1</text><text x="705" y="693">15</text>
    <text x="267" y="761">2</text><text x="294" y="808">3</text><text x="267" y="855">4</text>
    <text x="213" y="855">5</text><text x="186" y="808">6</text>
    <text x="415" y="600">9</text><text x="463" y="648">8</text><text x="415" y="696">7</text><text x="367" y="648">10</text>
    <text x="589" y="757">11</text><text x="631" y="817">12</text><text x="571" y="859">13</text><text x="529" y="799">14</text>
  </g>

  <g class="segment-labels" text-anchor="middle">
    <!-- supply -->
    <text class="seg-label" transform="translate(289 720) rotate(30)">Uncertain<tspan x="0" dy="9">monetary supply</tspan></text>
    <text class="seg-label" transform="translate(338 805) rotate(90)">Limited<tspan x="0" dy="9">food supply</tspan></text>
    <text class="seg-label" transform="translate(284 881) rotate(-30)">Perishability</text>
    <text class="seg-label" transform="translate(199 876) rotate(30)">Donor<tspan x="0" dy="9">constraints</tspan></text>
    <text class="seg-label" transform="translate(158 805) rotate(90)">Donor<tspan x="0" dy="9">relationships</tspan></text>
    <!-- demand -->
    <text class="seg-label" x="415" y="561">Client<tspan x="415" dy="9">choice</tspan></text>
    <text class="seg-label" transform="translate(503 645) rotate(90)">Limited<tspan x="0" dy="9">demand visibility</tspan></text>
    <text class="seg-label" x="415" y="715">Uncertain<tspan x="415" dy="9">demand</tspan></text>
    <text class="seg-label" transform="translate(327 645) rotate(-90)">Food<tspan x="0" dy="9">wastage</tspan></text>
    <!-- capacity -->
    <text class="seg-label" transform="translate(597 707) rotate(10)">Storage<tspan x="0" dy="8">• Cold</tspan><tspan x="0" dy="8">• Warehouse</tspan></text>
    <text class="seg-label" transform="translate(667 820) rotate(-80)">Transportation</text>
    <text class="seg-label" transform="translate(565 892) rotate(10)">Workforce</text>
    <text class="seg-label" transform="translate(501 791) rotate(100)">External<tspan x="0" dy="9">stakeholders</tspan></text>
  </g>

  <g class="workforce-list">
    <path d="M566 900 V970 M566 922 H573 M566 934 H573 M566 946 H573 M566 958 H573 M566 970 H573" stroke="#555" stroke-width="0.7" fill="none"/>
    <g fill="var(--orange)">
      <circle cx="576" cy="922" r="2.2"/><circle cx="576" cy="934" r="2.2"/><circle cx="576" cy="946" r="2.2"/>
      <circle cx="576" cy="958" r="2.2"/><circle cx="576" cy="970" r="2.2"/>
    </g>
    <g class="list-item">
      <text x="583" y="924">Volunteers</text><text x="583" y="936">Expertise and training</text>
      <text x="583" y="948">Attitudes and Beliefs</text><text x="583" y="960">Collaboration</text>
      <text x="583" y="972">Executive Support</text>
    </g>
  </g>

  <text class="title" x="432" y="1018" text-anchor="middle">Factors Affecting The Introducton Of Nutrition Policy</text>
</svg>
</div>
</body>
</html>
```